Our Velvetline

I am developing a web site which sells preowned high end designer handbags and accessories. Some of the brands include: Duvore, Marcel Ostrand & Velka, to name a few. I am after a luxurious and high end feel.

Some brands I like that express this feel include: Corvin, Velka, thecloset-kip.com, pursetradeorloan.com

I am after a logo, business card, letterhead, with compliments, address label and envelope designs.
The business name is Our velvetline, and the website will be www.ourvelvetline.com.au. I have thoughts of using OVL as a logo or OUR velvetline.com.au

I don't want a large logo, it needs to blend in with the name in some way - or may not need an image at all, if the style of the font speaks to the brand.

Thank-you

Reason: I would like to give designers plenty of time to be able to submit a design.

Target Market(s)

Women, aged 25-60 who are into fashion

Industry/Entity Type

Business

Requirements
Must have
• High End
Luxurious

```html
<!DOCTYPE html>
<html lang="en">
<head>
<meta charset="utf-8">
<title>Our Velvetline — With Compliments</title>
<link rel="stylesheet" href="https://fonts.googleapis.com/css2?family=Archivo:wght@800&display=swap">
<style>
  :root {
    --gold-text: #d9c98f;
    --grey-light: #f1f1f1;
    --grey-mid: #d4d4d4;
    --rule: #e6e6e6;
    --paper: #ffffff;
  }
  * { margin: 0; padding: 0; box-sizing: border-box; }
  html, body {
    width: 1200px;
    height: 567px;
    overflow: hidden;
    background: var(--paper);
  }
  .slip {
    position: relative;
    width: 1200px;
    height: 567px;
    background: var(--paper);
    font-family: "Archivo", Arial, sans-serif;
  }
  .band {
    position: absolute;
    left: 0;
    width: 1200px;
    height: 37px;
    background: linear-gradient(90deg, var(--grey-light) 0%, var(--grey-mid) 100%);
  }
  .band--top { top: 0; }
  .band--bottom { bottom: 0; }

  .slip-title {
    position: absolute;
    left: 46px;
    top: 60px;
    font-size: 28px;
    font-weight: 800;
    letter-spacing: 0.5px;
    color: var(--gold-text);
    text-decoration: underline;
    text-decoration-thickness: 2px;
    text-underline-offset: 4px;
  }

  .info {
    position: absolute;
    top: 395px;
    height: 104px;
    border-left: 2px solid var(--rule);
    font-size: 16px;
    font-weight: 800;
    line-height: 18.5px;
    color: var(--gold-text);
  }
  .info--contact { left: 48px; padding: 25px 0 0 15px; }
  .info--address { left: 405px; padding: 32px 0 0 17px; }

  .brand {
    position: absolute;
    left: 780px;
    top: 417px;
    width: 386px;
    height: 82px;
    display: flex;
    align-items: center;
    justify-content: flex-end;
    gap: 16px;
  }
  .brand-mark {
    width: 34px;
    height: 34px;
    background: var(--gold-text);
    flex: none;
  }
  .brand-name {
    font-size: 32px;
    font-weight: 800;
    color: var(--gold-text);
    white-space: nowrap;
  }
</style>
</head>
<body>
  <main class="slip">
    <div class="band band--top"></div>

    <h1 class="slip-title">WITH COMPLIMENTS</h1>

    <div class="info info--contact">
      <p>Phone: 420-517-000</p>
      <p>Fax: 420-517-001</p>
      <p>Email: mara@ourvelvetline.com.au</p>
    </div>

    <div class="info info--address">
      <p>Address: 248 Ashcombe Road,</p>
      <p>Elmsbury, VIC 3990</p>
    </div>

    <div class="brand">
      <span class="brand-mark" aria-hidden="true"></span>
      <span class="brand-name">Our Velvetline</span>
    </div>

    <div class="band band--bottom"></div>
  </main>
</body>
</html>
```